HIgh-end jewelry designer needs a business card design

I need a business card design for the ecclectic & rather expensive jewelry designs. My approach to my work is to combine very old jewelry offset with contemporary items. I enjoy the idea of legacy as well as repurposing finely crafted items that are not possible to create any longer. My desire is to celebrate the past in a contemporary & funky way. The name of my business is VELLORINE. I see my business card design as simple & yet enigmatic as possible. In the end... clean, simple & understated is the look I am after. Thank you for your consideration...

Target Market(s)

I will use this business card for the trade as well as customers

Industry/Entity Type

Business

Contact Information for Business Card

Marta Quorrin Owner/Designer 555-203-7718

Requirements
Must have
• Clean & simple sophisticated design using the word "Vellorinne" as the logo. I like the idea of a play on the word itself, perhaps even using different fonts (i.e.: a bold helvetica combined with a lovely script). I'm afraid to say more because I don't want to limit creative input. Gosh, sometimes it's ok to break the rules!
Nice to have
• In my mind, I have imagined this business card to be simple, using my company name "Vellorine" in a playful yet sophisticated manner. I believe that doing something beautifully simple can be a true challenge. I have imagined something with just black & white, however I am open to ideas... after all that's why I'm here!
Should not have
• As Mozart once said... "It has too many notes!" I know I'm being silly, but I don't want it to be complicated or overly ornate.

```html
<!DOCTYPE html>
<html lang="en">
<head>
<meta charset="utf-8">
<title>Vellorine — Business Card</title>
<link rel="stylesheet" href="https://fonts.googleapis.com/css2?family=Arimo:wght@400;700&display=swap">
<style>
  :root {
    --backdrop: #e4e2df;
    --card-black: #0b0b0b;
    --swoosh-grey: #a3a3a3;
    --text-grey: #9c9c9c;
    --wordmark-grey: #b4b4b4;
  }
  * { margin: 0; padding: 0; box-sizing: border-box; }
  html, body {
    width: 1200px;
    height: 800px;
    overflow: hidden;
    background: var(--backdrop);
  }
  .canvas {
    position: relative;
    width: 1200px;
    height: 800px;
    display: flex;
    align-items: center;
    justify-content: center;
  }
  .business-card {
    position: relative;
    width: 900px;
    height: 514px;
    background: var(--card-black);
    overflow: hidden;
    box-shadow: 0 10px 30px rgba(0, 0, 0, 0.18);
  }
  .swoosh {
    position: absolute;
    inset: 0;
    width: 900px;
    height: 514px;
  }
  .swoosh path { fill: var(--swoosh-grey); }
  .brand-wordmark {
    position: absolute;
    left: 70px;
    top: 268px;
    font-family: "Arimo", Arial, sans-serif;
    font-weight: 700;
    font-size: 50px;
    letter-spacing: 2px;
    color: var(--wordmark-grey);
  }
  .contact-block {
    position: absolute;
    left: 600px;
    width: 270px;
    top: 176px;
    text-align: center;
    font-family: "Arimo", Arial, sans-serif;
    font-weight: 400;
    color: var(--text-grey);
  }
  .contact-name {
    font-size: 29px;
    letter-spacing: 0.5px;
    margin-bottom: 16px;
  }
  .contact-role {
    font-size: 26px;
    margin-bottom: 16px;
  }
  .contact-phone {
    font-size: 26px;
  }
</style>
</head>
<body>
  <main class="canvas">
    <section class="business-card" aria-label="Vellorine business card">
      <svg class="swoosh" viewBox="0 0 900 514" aria-hidden="true">
        <path d="M95 514 C330 450 545 290 590 0 C562 180 535 370 562 514 Z"/>
      </svg>
      <div class="brand-wordmark">VELLORINE</div>
      <div class="contact-block">
        <p class="contact-name">MARTA QUORRIN</p>
        <p class="contact-role">Owner / Designer</p>
        <p class="contact-phone">555-203-7718</p>
      </div>
    </section>
  </main>
</body>
</html>
```